Interior Design/Decor and Staging Website

Current website: www.marlowcrestinteriors.example but need something lighter and more appealing. Logo is also being changed. I would like a clean cut look, modern and professional. Would like a slideshow for portfolio pictures, social media icons and logos of where the work has been featured: VORNA, Nest Wares, Durrandel, Tobias Quill, Plaza Furnishings, etc.

Target Market(s)

interior design and interior decor clients, both local and international.

Industry/Entity Type

Home Improvement

Number of Pages Required

5+ page

Font styles to use
Sans Serif

Requirements
Nice to have
• Testimonial page and Dwellr reviews.

```html
<!DOCTYPE html>
<html lang="en">
<head>
<meta charset="utf-8">
<title>Marlow Crest Interiors</title>
<link href="https://fonts.googleapis.com/css2?family=Roboto:wght@400;500;700&family=Open+Sans:ital,wght@0,400;0,600;0,700;1,400;1,700&display=swap" rel="stylesheet">
<style>
:root{
  --gold:#e9bc25;
  --gold-deep:#d9a91a;
  --ink:#1b1b1b;
  --ink-soft:#262626;
  --text:#333;
  --muted:#8a8a8a;
  --white:#fff;
  --line:#dcdcdc;
}
*{margin:0;padding:0;box-sizing:border-box}
html,body{width:1200px;height:3214px;overflow:hidden}
body{font-family:"Open Sans",Arial,sans-serif;color:var(--text);background:var(--white);position:relative}
section,header,footer{position:absolute;left:0;width:1200px}
.abs{position:absolute}
.section-title{position:absolute;left:0;width:1200px;text-align:center;font-family:"Roboto",Arial,sans-serif;font-size:26px;font-weight:400;color:#333;letter-spacing:.5px}
.section-title b{color:var(--gold);font-weight:700}
.section-lead{position:absolute;left:0;width:1200px;text-align:center;font-size:13px;line-height:24px;color:var(--muted)}

/* header */
.site-header{top:0;height:100px;background:#0c0c0c}
.brand{position:absolute;left:98px;top:22px;display:flex;align-items:center;gap:10px;color:var(--white);font-family:"Roboto",Arial,sans-serif;font-size:19px;line-height:21px;letter-spacing:.5px}
.brand-mark{width:16px;height:16px;border-radius:50%;background:var(--gold)}
.main-nav{position:absolute;right:98px;top:34px;display:flex;gap:18px}
.main-nav a{font-family:"Roboto",Arial,sans-serif;font-size:13px;color:var(--white);text-decoration:none;padding:8px 12px;border:1px solid transparent}
.main-nav a.active{border-color:var(--gold)}

/* hero */
.hero{top:100px;height:532px}
.hero-photo{position:absolute;inset:0;background:linear-gradient(90deg,#8a3a2a 0%,#a85a35 30%,#c88a3a 55%,#d9a83a 75%,#c9b9a4 100%)}
.hero-shade{position:absolute;inset:0;background:linear-gradient(180deg,rgba(0,0,0,.15),rgba(0,0,0,.25))}
.hero-title{position:absolute;left:160px;top:200px;font-family:"Roboto",Arial,sans-serif;font-weight:700;font-size:33px;color:var(--white)}
.hero-text{position:absolute;left:160px;top:252px;width:430px;font-size:13.5px;line-height:22px;color:var(--white)}
.slide-arrow{position:absolute}

/* welcome */
.welcome{top:632px;height:174px;background:var(--gold)}
.welcome h2{position:absolute;top:40px;width:1200px;text-align:center;font-family:"Roboto",Arial,sans-serif;font-size:25px;color:var(--white);font-weight:400}
.welcome h2 b{font-weight:700}
.welcome p{position:absolute;top:82px;left:0;width:1200px;text-align:center;font-size:14px;line-height:26px;color:var(--white)}

/* services */
.services{top:806px;height:559px}
.service-card{position:absolute;top:174px;width:312px}
.service-photo{height:182px;border:4px solid #eee}
.service-card h3{margin-top:32px;font-family:"Roboto",Arial,sans-serif;font-size:15px;font-weight:700;color:#222;letter-spacing:.5px}
.service-card p{margin-top:10px;font-size:12px;line-height:20px;color:#666}
.service-card a{display:block;margin-top:12px;font-size:11.5px;color:var(--gold);text-decoration:none}
.link-badge{position:absolute;left:134px;top:64px;width:44px;height:44px;border-radius:50%;background:#3a3222;display:flex;align-items:center;justify-content:center}

/* testimonials */
.testimonials{top:1365px;height:371px;background:linear-gradient(90deg,#2a2622,#3a342d 50%,#2b2724)}
.testimonials .section-title{top:40px;color:var(--white)}
.quote-mark{position:absolute;left:136px;top:96px;font-family:"Roboto",Arial,sans-serif;font-size:120px;font-weight:700;color:var(--white);line-height:1}
.client-photo{position:absolute;left:226px;top:110px;width:144px;height:144px;border-radius:50%;border:4px solid var(--white);background:radial-gradient(circle at 50% 45%,#e7c9a9,#c9a27a 60%,#8b7663)}
.testimonial-text{position:absolute;left:407px;top:103px;width:650px;font-size:12.5px;line-height:25px;font-style:italic;font-weight:700;color:var(--white)}
.stars{position:absolute;display:flex;gap:8px}
.testimonial-rule{position:absolute;left:407px;top:1648px;}
.client-name{position:absolute;left:407px;top:285px;font-size:12px;font-weight:700;font-style:italic;color:var(--gold)}
.client-role{position:absolute;left:407px;top:304px;font-size:12px;font-style:italic;color:var(--white)}
.dots{position:absolute;left:984px;top:250px;display:flex;gap:6px}
.dots span{width:10px;height:10px;border-radius:50%;border:1.5px solid var(--white)}
.dots span.on{background:var(--white)}

/* projects */
.projects{top:1736px;height:412px}
.project-strip{position:absolute;top:182px;left:0;display:flex}
.project-photo{width:240px;height:230px;border-right:2px solid #fff}

/* reviews */
.reviews{top:2148px;height:381px;background:var(--gold)}
.review-photo{position:absolute;left:99px;top:59px;width:443px;height:264px;border:5px solid #c99d18;background:linear-gradient(135deg,#7b5a3a,#d8cfbd 45%,#f1ece2 70%,#a58a62)}
.review-title{position:absolute;left:579px;top:58px;font-family:"Roboto",Arial,sans-serif;font-size:25px;color:var(--white);font-weight:400}
.review-title b{font-weight:700}
.review-meta{position:absolute;left:579px;top:96px;display:flex;gap:22px;font-size:13px;font-weight:700;color:var(--white);align-items:center}
.review-meta span{display:flex;align-items:center;gap:8px}
.review-text{position:absolute;left:579px;width:580px;font-size:12.5px;line-height:24px;color:var(--white)}

/* clients */
.clients{top:2529px;height:317px}
.client-box{position:absolute;top:173px;width:178px;height:88px;border:1px solid var(--line);display:flex;align-items:center;justify-content:center;gap:8px;font-family:"Open Sans",Arial,sans-serif;font-size:17px;font-weight:700;color:#444}
.client-box i{width:10px;height:10px;background:#444;display:block}

/* footer */
.site-footer{top:2846px;height:309px;background:#1c1c1c}
.footer-col{position:absolute;top:42px}
.footer-col h4{font-family:"Roboto",Arial,sans-serif;font-size:14px;font-weight:700;color:var(--white);letter-spacing:.3px;padding-bottom:14px;margin-bottom:14px;border-bottom:1px solid #333;width:170px}
.footer-col ul{list-style:none}
.footer-col li{font-size:12.5px;color:#bbb;line-height:27px}
.footer-col li::before{content:"»";color:var(--gold);margin-right:20px;font-weight:700}
.contact-text{font-size:12.5px;line-height:21px;color:#bbb}
.contact-row{display:flex;align-items:center;gap:12px;margin-top:12px;font-size:12.5px;color:#bbb}
.contact-row.phone{font-family:"Roboto",Arial,sans-serif;font-size:20px;font-weight:700;color:var(--gold);margin-top:8px}
.footer-bar{top:3155px;height:59px;background:#0e0e0e;font-size:12px;color:#aaa}
.footer-bar .copy{position:absolute;left:98px;top:21px}
.footer-bar .code{position:absolute;right:40px;top:21px}
</style>
</head>
<body>

<header class="site-header">
  <div class="brand"><span class="brand-mark"></span><span>MARLOW CREST<br>INTERIORS</span></div>
  <nav class="main-nav">
    <a class="active" href="#">HOME</a><a href="#">SERVICES</a><a href="#">GALLERY</a><a href="#">CONTACT</a>
  </nav>
</header>

<section class="hero">
  <div class="hero-photo" role="img" aria-label="Dining room with wooden table, chairs, wall art and warm red and yellow walls"></div>
  <div class="hero-shade"></div>
  <h1 class="hero-title">MARLOW CREST INTERIORS</h1>
  <p class="hero-text">We are an Interior Design/Decor and Staging company.Have your house professionally decorated for a quicker sale Decor outdated? Need new flooring or kitchen cabinets? We can help you.</p>
  <svg class="slide-arrow" style="left:56px;top:236px" width="30" height="64" viewBox="0 0 30 64"><polyline points="28,2 2,32 28,62" fill="none" stroke="#fff" stroke-opacity=".7" stroke-width="2"/></svg>
  <svg class="slide-arrow" style="right:56px;top:236px" width="30" height="64" viewBox="0 0 30 64"><polyline points="2,2 28,32 2,62" fill="none" stroke="#fff" stroke-opacity=".7" stroke-width="2"/></svg>
</section>

<section class="welcome">
  <h2><b>WELCOME TO</b> MARLOW CREST INTERIORS</h2>
  <p>We are an Interior Design/Decor and Staging company.Have your house professionally decorated for a quicker sale.<br>Decor outdated? Need new flooring or kitchen cabinets? We can help you.</p>
</section>

<section class="services">
  <h2 class="section-title" style="top:48px"><b>OUR</b> SERVICES</h2>
  <p class="section-lead" style="top:94px">We are an Interior Design/Decor and Staging company.Have your house professionally decorated for a quicker sale.<br>Decor outdated? Need new flooring or kitchen cabinets? We can help you.</p>

  <article class="service-card" style="left:107px">
    <div class="service-photo" role="img" aria-label="Bright living room with curved staircase and plants" style="background:linear-gradient(135deg,#f3f1ea,#d9d6cc 50%,#8c9a76)"></div>
    <h3>INTERIOR DECOR</h3>
    <p>Whether your room is empty or you have some of the furniture, we are here to help you achieve the look you have been dreaming of from Coastal...</p>
    <a href="#">Read More &gt;</a>
  </article>

  <article class="service-card" style="left:446px">
    <div class="service-photo" role="img" aria-label="Staged room with warm golden overlay" style="background:linear-gradient(135deg,#e6c453,#d7b23a 60%,#c9a130);position:relative">
      <span class="link-badge"><svg width="20" height="20" viewBox="0 0 20 20"><g fill="none" stroke="#e9bc25" stroke-width="2.4" stroke-linecap="round"><path d="M8 12l4-4"/><path d="M9 5.5l1.5-1.5a3.2 3.2 0 014.5 4.5L13.5 10"/><path d="M11 14.5L9.5 16a3.2 3.2 0 01-4.5-4.5L6.5 10"/></g></svg></span>
    </div>
    <h3>HOME STAGING</h3>
    <p>Let us help you with the sale of your residence. Home Staging will make your house more appealing to buyers, accelerating the sale process ...</p>
    <a href="#">Read More &gt;</a>
  </article>

  <article class="service-card" style="left:781px">
    <div class="service-photo" role="img" aria-label="Designer reviewing plans with clients" style="background:linear-gradient(135deg,#e9e2d8,#c99c7e 50%,#8a5a44)"></div>
    <h3>RESTYLE &amp; REDESIGN</h3>
    <p>Is your current decor outdated? Do you need help with new countertops, cabinetry or flooring? Whether you need to update the decor style...</p>
    <a href="#">Read More &gt;</a>
  </article>
</section>

<section class="testimonials" role="img" aria-label="Dimmed background of smiling group">
  <h2 class="section-title"><b>CLIENT</b> TESTIMONIALS</h2>
  <div class="quote-mark">&ldquo;</div>
  <div class="client-photo" role="img" aria-label="Portrait of the client"></div>
  <p class="testimonial-text">Lorem ipsum dolor sit amet, consectetur adipisicing elit, sed do eiusmod tempor incididunt ut labore et dolore magna aliqua. Ut enim ad minim veniam, quis nostrud exercitation ullamco laboris nisi ut aliquip ex ea commodo consequat. Duis aute irure dolor in reprehenderit in voluptate velit esse cillum dolore eu fugiat nulla pariatur. Excepteur sint occaecat cupidatat non proident ,</p>
  <div class="stars" style="left:407px;top:230px">
    <svg width="96" height="18" viewBox="0 0 96 18"><g fill="#e9bc25"><path id="st" d="M9 0l2.6 5.8 6.4.6-4.8 4.2 1.4 6.3L9 13.6 3.4 16.9l1.4-6.3L0 6.4l6.4-.6z"/><use href="#st" x="20"/><use href="#st" x="40"/><use href="#st" x="60"/><use href="#st" x="78"/></g></svg>
  </div>
  <svg class="abs" style="left:407px;top:268px" width="220" height="2"><line x1="0" y1="1" x2="220" y2="1" stroke="#fff" stroke-opacity=".5"/></svg>
  <div class="client-name">DANA WHITCOMBE</div>
  <div class="client-role">Manager</div>
  <div class="dots"><span></span><span></span><span></span><span class="on"></span></div>
</section>

<section class="projects">
  <h2 class="section-title" style="top:52px"><b>RECENT</b> PROJECTS</h2>
  <p class="section-lead" style="top:97px">We are an Interior Design/Decor and Staging company.Have your house professionally decorated for a quicker sale.<br>Decor outdated? Need new flooring or kitchen cabinets? We can help you.</p>
  <div class="project-strip">
    <div class="project-photo" role="img" aria-label="Bedroom with pink curtains and chandelier" style="background:linear-gradient(135deg,#efe7df,#d8b9b0 50%,#b49a7a)"></div>
    <div class="project-photo" role="img" aria-label="Living room with red sofa and patterned rug" style="background:linear-gradient(135deg,#b89a6a,#a53a2c 55%,#6d4a2e)"></div>
    <div class="project-photo" role="img" aria-label="Sunlit sitting room with round table and flowers" style="background:linear-gradient(135deg,#e7cf9a,#f0e6cf 50%,#b08a4e)"></div>
    <div class="project-photo" role="img" aria-label="Dining area with chandelier and wood floor" style="background:linear-gradient(135deg,#f1efe8,#cfc6b6 50%,#7b5a3a)"></div>
    <div class="project-photo" role="img" aria-label="Child's bedroom with white dresser" style="background:linear-gradient(135deg,#f3f2ee,#d9d5cb 55%,#b7b0a2)"></div>
  </div>
  <svg class="abs" style="right:16px;top:276px" width="14" height="26" viewBox="0 0 14 26"><polyline points="2,2 12,13 2,24" fill="none" stroke="#fff" stroke-width="2"/></svg>
</section>

<section class="reviews">
  <svg class="abs" style="left:34px;top:158px" width="26" height="56" viewBox="0 0 26 56"><polyline points="24,2 2,28 24,54" fill="none" stroke="#fff" stroke-width="2"/></svg>
  <svg class="abs" style="right:34px;top:158px" width="26" height="56" viewBox="0 0 26 56"><polyline points="2,2 24,28 2,54" fill="none" stroke="#fff" stroke-width="2"/></svg>
  <div class="review-photo" role="img" aria-label="Entry table with lamps, plant and dining room beyond"></div>
  <h2 class="review-title"><b>OUR DWELLR</b> REVIEWS</h2>
  <div class="review-meta">
    <span><svg width="16" height="14" viewBox="0 0 16 14"><path d="M1 2h5l1.5 2H15v9H1z" fill="none" stroke="#fff" stroke-width="1.5"/></svg>RESIDENTIAL</span>
    <span><svg width="18" height="14" viewBox="0 0 18 14"><path d="M2 1h10a1.5 1.5 0 011.5 1.5v5A1.5 1.5 0 0112 9H6l-3 3V9H2A1.5 1.5 0 01.5 7.5v-5A1.5 1.5 0 012 1z" fill="#fff"/></svg>5 COMMENTS</span>
  </div>
  <div class="stars" style="left:579px;top:124px">
    <svg width="112" height="20" viewBox="0 0 112 20"><g fill="#fff"><path id="rs" d="M10 0l2.9 6.3 7.1.7-5.3 4.7 1.5 7L10 15.1 3.8 18.7l1.5-7L0 7l7.1-.7z"/><use href="#rs" x="23"/><use href="#rs" x="46"/><use href="#rs" x="69"/><use href="#rs" x="92"/></g></svg>
  </div>
  <p class="review-text" style="top:160px">We are an Interior Design/Decor and Staging company.Have your house profession-ally decorated for a quicker sale. Decor outdated? Need new flooring or kitchen cabinets? We can help you.</p>
  <p class="review-text" style="top:232px">Lorem ipsum dolor sit amet, consectetur adipisicing elit, sed do eiusmod tempor incid-idunt ut labore et dolore magna aliqua. Ut enim ad minim veniam, quis nostrud llamco laboris nisi ut aliquip ex ea commodo consequat. Duis aute irure dolor in in voluptate velit esse cillum dolore eu fugiat nulla pariatur.</p>
</section>

<section class="clients">
  <h2 class="section-title" style="top:44px"><b>OUR</b> CLIENTS</h2>
  <p class="section-lead" style="top:89px">We are an Interior Design/Decor and Staging company.Have your house professionally decorated for a quicker sale.<br>Decor outdated? Need new flooring or kitchen cabinets? We can help you.</p>
  <svg class="abs" style="left:76px;top:200px" width="18" height="36" viewBox="0 0 18 36"><polyline points="16,2 2,18 16,34" fill="none" stroke="#ccc" stroke-width="2"/></svg>
  <svg class="abs" style="right:76px;top:200px" width="18" height="36" viewBox="0 0 18 36"><polyline points="2,2 16,18 2,34" fill="none" stroke="#ccc" stroke-width="2"/></svg>
  <div class="client-box" style="left:118px"><i></i>VORNA</div>
  <div class="client-box" style="left:315px">Nest Wares</div>
  <div class="client-box" style="left:510px">Tobias Quill</div>
  <div class="client-box" style="left:705px">Fernhollow</div>
  <div class="client-box" style="left:902px">Durrandel</div>
</section>

<footer class="site-footer">
  <div class="footer-col" style="left:98px">
    <h4>INFORMATION</h4>
    <ul><li>Home</li><li>Our drone</li><li>Where to buy / order it?</li><li>Show us your race</li><li>Community Forum</li><li>News</li></ul>
  </div>
  <div class="footer-col" style="left:380px">
    <h4>CONTACT US</h4>
    <p class="contact-text">Lorem ipsum dolor sit amet elit,<br>sed do eiusmod tempor.</p>
    <div class="contact-row"><svg width="16" height="12" viewBox="0 0 16 12"><rect x=".75" y=".75" width="14.5" height="10.5" fill="none" stroke="#999" stroke-width="1.5"/><polyline points="1,1 8,7 15,1" fill="none" stroke="#999" stroke-width="1.5"/></svg>hello@marlowcrestinteriors.example</div>
    <div class="contact-row phone"><svg width="16" height="16" viewBox="0 0 16 16"><path d="M3 1l3 3-1.5 2a9 9 0 005.5 5.5L12 10l3 3-2 2C7 15 1 9 1 3z" fill="#999"/></svg>555-014-2278</div>
  </div>
  <div class="footer-col" style="left:661px">
    <h4>SUPPORT LINKS</h4>
    <ul><li>Privacy Policy</li><li>Terms &amp; Condition</li><li>Site Map</li></ul>
  </div>
  <div class="footer-col" style="left:912px">
    <h4>SOCIAL MEDIA LINKS</h4>
    <ul><li>Circlepage</li><li>Chirpline</li><li>Linkwork</li><li>Plusroom</li><li>Reelcast</li></ul>
  </div>
</footer>
<div class="abs footer-bar" style="left:0;width:1200px">
  <span class="copy">Copyright &copy; 2016 Marlow Crest Interiors.All rights reserved.</span>
  <span class="code">C14</span>
</div>

</body>
</html>
```